Business cards for a naturopathic day clinic for stem cell therapy

We need a basic design for a day clinic, that offers stem cell therapies for Lyme therapy and other severe chronic illnesses.
Our name is "Casa velorìn", which can be translated into "Manor Velorbloom". We are a couple of naturopaths working along side physiotherapists and osteopaths, yoga teachers and massage therapists. I attached our logo.

```html
<!DOCTYPE html>
<html lang="en">
<head>
<meta charset="utf-8">
<title>Casa velorìn – Business Cards</title>
<link href="https://fonts.googleapis.com/css2?family=Montserrat:wght@400;500;700&display=swap" rel="stylesheet">
<style>
  :root {
    --stage: #636363;
    --card: #1d1d1d;
    --lime: #b4cc4c;
    --text: #f2f2f2;
    --muted: #b9b9b9;
    --silver: #c9c9c9;
  }
  * { margin: 0; padding: 0; box-sizing: border-box; }
  html, body { width: 1200px; height: 801px; overflow: hidden; }
  body {
    background: var(--stage);
    font-family: "Montserrat", sans-serif;
    display: flex;
    align-items: center;
    justify-content: center;
    gap: 48px;
  }
  .card {
    width: 520px;
    height: 300px;
    background: var(--card);
    border-radius: 16px;
    border-bottom: 2px solid var(--lime);
    border-left: 1px solid var(--lime);
    box-shadow: 0 18px 30px rgba(0,0,0,.35);
    position: relative;
    overflow: hidden;
  }
  /* Front */
  .card--front { display: flex; align-items: center; }
  .brand {
    width: 250px;
    display: flex;
    align-items: center;
    justify-content: center;
    gap: 12px;
    padding-left: 18px;
  }
  .brand__dot {
    width: 14px; height: 14px;
    border-radius: 50%;
    background: var(--lime);
    flex: none;
  }
  .brand__name {
    font-size: 30px;
    font-weight: 400;
    color: var(--lime);
    letter-spacing: .5px;
    white-space: nowrap;
  }
  .divider {
    width: 1px;
    height: 170px;
    background: var(--lime);
    flex: none;
  }
  .details { padding-left: 26px; }
  .details__name {
    color: var(--lime);
    font-weight: 700;
    font-size: 19px;
    letter-spacing: .3px;
  }
  .details__role {
    color: var(--text);
    font-size: 11px;
    letter-spacing: .6px;
    margin-bottom: 14px;
  }
  .details__address {
    color: var(--text);
    font-size: 11px;
    line-height: 1.45;
    margin-bottom: 10px;
  }
  .contact { list-style: none; }
  .contact li {
    color: var(--text);
    font-size: 11px;
    line-height: 1.7;
    display: flex;
    align-items: center;
    gap: 7px;
  }
  .contact svg { width: 10px; height: 10px; flex: none; }
  /* Back */
  .card--back {
    display: flex;
    align-items: center;
    justify-content: center;
    gap: 18px;
  }
  .card--back .brand__dot {
    width: 34px; height: 34px;
    border: 3px solid var(--silver);
    background: var(--lime);
  }
  .card--back .brand__name {
    font-size: 46px;
    color: var(--silver);
  }
</style>
</head>
<body>

  <section class="card card--front" aria-label="Business card front">
    <div class="brand">
      <span class="brand__dot"></span>
      <span class="brand__name">Casa velorìn</span>
    </div>
    <div class="divider"></div>
    <div class="details">
      <p class="details__name">JONAS ALBRECHT</p>
      <p class="details__role">DIRECTOR</p>
      <p class="details__address">Lindenweg 7,<br>35410 Hollstadt, Germany</p>
      <ul class="contact">
        <li>
          <svg viewBox="0 0 10 10"><path d="M2 1l2 2-1 1.2a6 6 0 0 0 2.8 2.8L7 6l2 2-1.2 1.2C4.5 9 1 5.5.8 2.2z" fill="var(--lime)"/></svg>
          +49 6100 5550182
        </li>
        <li>
          <svg viewBox="0 0 10 10"><rect x="1" y="3" width="8" height="6" rx="1" fill="var(--lime)"/><rect x="3" y="1" width="4" height="3" fill="var(--lime)"/></svg>
          06100 5550247
        </li>
        <li>
          <svg viewBox="0 0 10 10"><rect x="1" y="2" width="8" height="6" fill="none" stroke="var(--lime)" stroke-width="1"/><path d="M1 2l4 3.5L9 2" fill="none" stroke="var(--lime)" stroke-width="1"/></svg>
          info@casa-velorin.de
        </li>
        <li>
          <svg viewBox="0 0 10 10"><circle cx="5" cy="5" r="4" fill="none" stroke="var(--lime)" stroke-width="1"/><path d="M1 5h8M5 1c-2 2.5-2 5.5 0 8M5 1c2 2.5 2 5.5 0 8" fill="none" stroke="var(--lime)" stroke-width=".8"/></svg>
          www.casa-velorin.de
        </li>
      </ul>
    </div>
  </section>

  <section class="card card--back" aria-label="Business card back">
    <span class="brand__dot"></span>
    <span class="brand__name">Casa velorìn</span>
  </section>

</body>
</html>
```